Harvest Cellar

We need desigin for our main page(concept will be used for other pages also).
We already have a logo, and moqup of our main page(see attch).
You could change layers and positions on moqup, but please use logo, and its colors in design creating. (We have logo in different colors, i attached 2 samples, so you could use also another colors if you wish).

Our bussinees will be something similar to BloomLaunch or Seedwell.io, but with some special features. So main idea: start-ups, donations, investemnets

Designs were prefer:
http://seedwell.io/
http://www.bloomlaunch-example.com/

Brief was updated.

Target Market(s)

Clients are middle aged persons, who interested in new start-ups, investments and so on.

Requirements
Must have
• Design must be neat

```html
<!DOCTYPE html>
<html lang="en">
<head>
<meta charset="utf-8">
<title>Harvest Cellar</title>
<link href="https://fonts.googleapis.com/css2?family=Noto+Serif:wght@400;700&family=Open+Sans:wght@400;600;700&display=swap" rel="stylesheet">
<style>
:root{
  --red:#c9191f;
  --red-dark:#a8121a;
  --charcoal:#3d3d3d;
  --topbar:#505050;
  --panel:#e6e6e6;
  --section:#f3f3f3;
  --text:#444;
  --muted:#777;
  --line:#d6d6d6;
  --white:#fff;
  --star:#f5c61f;
}
*{box-sizing:border-box;margin:0;padding:0}
html,body{width:876px;height:1200px;overflow:hidden}
body{position:relative;background:var(--white);font-family:"Noto Serif",serif;color:var(--text)}
.abs{position:absolute}
.topbar{left:0;top:0;width:876px;height:29px;background:var(--topbar)}
.logo{left:95px;top:43px;width:159px;height:58px;background:linear-gradient(90deg,#bdbdbd,#f4f4f4 55%,#c4c4c4);display:flex;align-items:center;justify-content:center;gap:6px;font-family:"Open Sans",sans-serif;font-weight:700;font-size:14px;color:var(--red)}
.logo i{width:10px;height:10px;background:var(--red);border-radius:50%}
.nav{top:49px;height:49px;background:var(--charcoal);color:#eee;font:400 9px "Open Sans",sans-serif;display:flex;align-items:center;justify-content:center;border-radius:2px}
.search{left:621px;top:48px;width:159px;height:18px;background:#eaeaea;border:1px solid #ddd;font:400 6px "Open Sans",sans-serif;color:#999;padding:5px 6px}
.search svg{position:absolute;right:5px;top:4px}
.lang-label{left:620px;top:80px;font:400 7px "Open Sans",sans-serif;color:#999}
.lang{left:699px;top:74px;width:81px;height:20px;border:1px solid #ddd;background:#f4f4f4;font:400 8px "Open Sans",sans-serif;color:#888;display:flex;align-items:center;padding-left:8px;gap:4px}
.lang .flag{width:18px;height:10px;background:#2b3f8c;border:1px solid #c33}
.lang .caret{margin-left:auto;margin-right:8px;border:4px solid transparent;border-top:5px solid #555;margin-top:4px}
.stats{left:95px;top:112px;width:159px;height:259px;background:var(--red);border-radius:3px;list-style:none}
.stats li{height:35px;border-bottom:1px solid #a9141a;display:flex;align-items:center;padding-left:4px;color:var(--white);font-size:9.5px}
.stats li:last-child{border:none}
.stats svg{margin-right:7px;flex:none}
.video{left:270px;top:112px;width:337px;height:232px;background:#f0f0f0;padding:5px}
.video .shot{width:100%;height:222px;background:linear-gradient(100deg,#f6efe2 0%,#eadfce 45%,#9a7a68 70%,#d9cbbd 100%)}
.play-big{left:132px;top:103px;width:66px;height:38px;background:rgba(50,50,50,.9);border-radius:3px}
.controls{left:12px;top:202px;width:320px;height:24px}
.ctrl-play{left:0;top:0;width:40px;height:22px;background:var(--charcoal);border-radius:2px}
.ctrl-bar{left:48px;top:0;width:272px;height:22px;background:#333;border-radius:2px}
.track{left:8px;top:10px;width:190px;height:3px;background:#777}
.track b{display:block;width:132px;height:3px;background:#f29b1c}
.hd{right:8px;top:5px;font:700 8px "Open Sans",sans-serif;color:#eee;font-style:normal}
.login{left:621px;top:112px;width:159px;height:222px;background:var(--panel);border-radius:3px}
.tab{top:0;height:27px;width:80px;color:var(--white);font:400 8.5px "Open Sans",sans-serif;display:flex;align-items:center;justify-content:center}
.tab-a{left:0;background:var(--red)}
.tab-b{left:82px;width:77px;background:var(--red-dark)}
.login label{position:absolute;left:9px;font:400 8px "Open Sans",sans-serif;color:#888}
.login .field{left:9px;width:143px;height:24px;background:#f2f2f2;border-top:2px solid #d2d2d2}
.check{left:13px;font:400 8px "Open Sans",sans-serif;color:#888;display:flex;align-items:center;gap:3px}
.login-btn{left:48px;top:161px;width:59px;height:19px;background:var(--red);border-radius:3px;color:var(--white);font:700 8.5px "Open Sans",sans-serif;display:flex;align-items:center;justify-content:center}
.projects{left:0;top:390px;width:876px;height:540px;background:var(--section)}
.filter{top:16px;width:103px;height:35px;background:var(--charcoal);color:var(--white);font-size:9.5px;display:flex;align-items:center;justify-content:center;border-radius:2px}
.filter.active{background:var(--red)}
.card{top:76px;width:161px;height:322px;background:var(--white);border:1px solid #e0e0e0;border-radius:3px;text-align:center}
.stars{position:absolute;top:6px;left:0;width:100%;display:flex;justify-content:center;gap:2px}
.card h3{position:absolute;top:34px;width:100%;color:var(--red);font-size:12.5px;font-weight:700}
.card .pic{position:absolute;left:18px;top:60px;width:125px;height:94px;border-radius:2px}
.card p{position:absolute;left:14px;top:163px;width:133px;font-size:7px;line-height:10px;color:#555}
.progress{position:absolute;left:15px;top:208px;width:132px;height:8px;background:#ddd;border-radius:4px}
.progress b{position:absolute;right:0;top:0;height:8px;width:52px;background:var(--red);border-radius:4px;color:#fff;font:400 6px "Noto Serif",serif;line-height:8px;font-weight:400}
.invested{position:absolute;left:26px;top:224px;width:108px;height:22px;background:var(--charcoal);color:var(--white);border-radius:3px;font:700 9.5px "Open Sans",sans-serif;line-height:22px}
.mini{position:absolute;top:258px;width:60px;height:18px;background:var(--charcoal);color:#eee;border-radius:3px;font-size:6.5px;line-height:18px}
.invest-btn{position:absolute;left:39px;top:286px;width:81px;height:16px;background:var(--red);color:var(--white);border-radius:2px;font:700 9px "Open Sans",sans-serif;line-height:16px}
.more{left:314px;top:425px;width:249px;height:99px;background:var(--red);border-radius:2px;color:var(--white);text-align:center}
.more h2{font-size:20px;font-weight:400;margin-top:13px}
.more span{display:block;font-size:12px;margin-top:3px}
.more svg{margin-top:5px}
.about{left:0;top:930px;width:876px;height:206px;background:linear-gradient(#e9e9e9,#fff 40px)}
.about h4{position:absolute;top:44px;font-size:9.5px;font-weight:400;color:#333;border-bottom:1px solid var(--line);padding-bottom:3px}
.about .photo{position:absolute;top:62px;height:75px}
.about .body{position:absolute;top:61px;font-size:8px;line-height:13.2px;color:#555;text-align:justify}
.about .read{position:absolute;top:184px;font-size:8px;color:var(--red)}
.footer{left:0;top:1136px;width:876px;height:64px;background:var(--topbar);color:var(--white)}
.social{left:96px;top:22px;display:flex;gap:4px}
.social i{width:22px;height:22px;border-radius:50%;background:var(--white)}
.links{left:0;top:16px;width:876px;text-align:center;font-size:8px;word-spacing:2px}
.links span{margin:0 8px}
.copy{left:0;top:36px;width:876px;text-align:center;font-size:7.5px}
</style>
</head>
<body>
<div class="abs topbar"></div>

<div class="abs logo"><i></i>Harvest Cellar</div>

<div class="abs nav" style="left:282px;width:102px">How It Works?</div>
<div class="abs nav" style="left:390px;width:103px">Project Review</div>
<div class="abs nav" style="left:498px;width:101px">Virtual Office</div>

<div class="abs search">Type search
  <svg width="9" height="9" viewBox="0 0 10 10"><circle cx="4" cy="4" r="3" fill="none" stroke="#999" stroke-width="1.2"/><line x1="6.3" y1="6.3" x2="9" y2="9" stroke="#999" stroke-width="1.4"/></svg>
</div>
<div class="abs lang-label">Select your Language</div>
<div class="abs lang"><span class="flag"></span>English<span class="caret"></span></div>

<ul class="abs stats">
  <li><svg width="15" height="15" viewBox="0 0 16 16"><circle cx="8" cy="8" r="7.5" fill="#fff"/><path d="M4.5 8.2l2.4 2.4 4.6-5" fill="none" stroke="#c9191f" stroke-width="2"/></svg>$ 50,000,000 of investments</li>
  <li><svg width="15" height="15" viewBox="0 0 16 16"><circle cx="8" cy="8" r="7.5" fill="#fff"/><path d="M4.5 8.2l2.4 2.4 4.6-5" fill="none" stroke="#c9191f" stroke-width="2"/></svg>1600 Start -Ups</li>
  <li><svg width="15" height="15" viewBox="0 0 16 16"><circle cx="8" cy="8" r="7.5" fill="#fff"/><path d="M4.5 8.2l2.4 2.4 4.6-5" fill="none" stroke="#c9191f" stroke-width="2"/></svg>700 Organisations</li>
  <li><svg width="15" height="15" viewBox="0 0 16 16"><circle cx="8" cy="8" r="7.5" fill="#fff"/><path d="M4.5 8.2l2.4 2.4 4.6-5" fill="none" stroke="#c9191f" stroke-width="2"/></svg>10,000 Investors</li>
  <li><svg width="15" height="15" viewBox="0 0 16 16"><circle cx="8" cy="8" r="7.5" fill="#fff"/><path d="M4.5 8.2l2.4 2.4 4.6-5" fill="none" stroke="#c9191f" stroke-width="2"/></svg>5000 Employees</li>
  <li><svg width="15" height="15" viewBox="0 0 16 16"><circle cx="8" cy="8" r="7.5" fill="#fff"/><path d="M4.5 8.2l2.4 2.4 4.6-5" fill="none" stroke="#c9191f" stroke-width="2"/></svg>2000 Partners</li>
  <li><svg width="15" height="15" viewBox="0 0 16 16"><circle cx="8" cy="8" r="7.5" fill="#fff"/><path d="M4.5 8.2l2.4 2.4 4.6-5" fill="none" stroke="#c9191f" stroke-width="2"/></svg>$ 10,000,000 of profit</li>
</ul>

<div class="abs video">
  <div class="shot" role="img" aria-label="Promotional video still of a smiling woman sitting in a bright room"></div>
  <div class="abs play-big"><svg width="66" height="38" viewBox="0 0 66 38"><path d="M28 12l12 7-12 7z" fill="#fff"/></svg></div>
  <div class="abs controls">
    <div class="abs ctrl-play"><svg width="40" height="22" viewBox="0 0 40 22"><path d="M17 6l8 5-8 5z" fill="#fff"/></svg></div>
    <div class="abs ctrl-bar">
      <div class="abs track"><b></b></div>
      <i class="abs hd">HD ⛶</i>
    </div>
  </div>
</div>

<div class="abs login">
  <div class="abs tab tab-a">Login</div>
  <div class="abs tab tab-b">Registration</div>
  <label style="top:40px">E-mail or Phone</label>
  <div class="abs field" style="top:57px"></div>
  <label style="top:92px">Password</label>
  <div class="abs field" style="top:108px"></div>
  <div class="abs check" style="top:144px"><svg width="10" height="9" viewBox="0 0 10 9"><rect x=".5" y="1.5" width="7" height="7" fill="none" stroke="#888"/><path d="M2 4.5l2 2 5-6" fill="none" stroke="#666" stroke-width="1.2"/></svg>Forgot Password</div>
  <div class="abs login-btn">LOGIN</div>
  <div class="abs check" style="top:193px"><svg width="10" height="9" viewBox="0 0 10 9"><rect x=".5" y="1.5" width="7" height="7" fill="none" stroke="#888"/><path d="M2 4.5l2 2 5-6" fill="none" stroke="#666" stroke-width="1.2"/></svg>Safe Login</div>
</div>

<section class="abs projects">
  <div class="abs filter active" style="left:95px">Recommended</div>
  <div class="abs filter" style="left:290px">Popular</div>
  <div class="abs filter" style="left:483px">Most Viewed</div>
  <div class="abs filter" style="left:678px">New</div>

  <article class="abs card" style="left:95px">
    <div class="stars"><svg width="88" height="15" viewBox="0 0 88 15"><g fill="#f5c61f" stroke="#d9a80f" stroke-width=".5"><path id="st" d="M7.5 .5l2.1 4.6 5 .5-3.8 3.4 1.1 5-4.4-2.6-4.4 2.6 1.1-5L.2 5.6l5-.5z"/><use href="#st" x="18"/><use href="#st" x="36"/><use href="#st" x="54"/><use href="#st" x="72"/></g></svg></div>
    <h3>Project A</h3>
    <div class="pic" role="img" aria-label="Close-up of a gold padlock on a credit card" style="background:linear-gradient(135deg,#c9c9c9,#e2b23a 45%,#a67612)"></div>
    <p>Lorem ipsum dolor sit amet, consectetur adipisicing elit, sed do eiusmod tempor incididunt ut labore et dolore magna aliqua.</p>
    <div class="progress"><b>70 % Success</b></div>
    <div class="invested">90,000 Invested</div>
    <div class="mini" style="left:15px">23,000 Invested</div>
    <div class="mini" style="left:86px">23 Days Left</div>
    <div class="invest-btn">Invest</div>
  </article>

  <article class="abs card" style="left:270px">
    <div class="stars"><svg width="88" height="15" viewBox="0 0 88 15"><g fill="#f5c61f" stroke="#d9a80f" stroke-width=".5"><use href="#st"/><use href="#st" x="18"/><use href="#st" x="36"/><use href="#st" x="54"/><use href="#st" x="72"/></g></svg></div>
    <h3>Project B</h3>
    <div class="pic" role="img" aria-label="Blue combination padlock resting on banknotes" style="background:linear-gradient(135deg,#b9b7a8,#3d9ad6 50%,#8c8a7a)"></div>
    <p>Lorem ipsum dolor sit amet, consectetur adipisicing elit, sed do eiusmod tempor incididunt ut labore et dolore magna aliqua.</p>
    <div class="progress"><b>70 % Success</b></div>
    <div class="invested">90,000 Invested</div>
    <div class="mini" style="left:15px">23,000 Invested</div>
    <div class="mini" style="left:86px">23 Days Left</div>
    <div class="invest-btn">Invest</div>
  </article>

  <article class="abs card" style="left:444px">
    <div class="stars"><svg width="88" height="15" viewBox="0 0 88 15"><g fill="#f5c61f" stroke="#d9a80f" stroke-width=".5"><use href="#st"/><use href="#st" x="18"/><use href="#st" x="36"/><use href="#st" x="54"/><use href="#st" x="72"/></g></svg></div>
    <h3>Project C</h3>
    <div class="pic" role="img" aria-label="Stack of gold coins on green banknotes" style="background:linear-gradient(135deg,#5f6a3a,#c9a34a 40%,#4d7a3a 80%)"></div>
    <p>Lorem ipsum dolor sit amet, consectetur adipisicing elit, sed do eiusmod tempor incididunt ut labore et dolore magna aliqua.</p>
    <div class="progress"><b>70 % Success</b></div>
    <div class="invested">90,000 Invested</div>
    <div class="mini" style="left:15px">23,000 Invested</div>
    <div class="mini" style="left:86px">23 Days Left</div>
    <div class="invest-btn">Invest</div>
  </article>

  <article class="abs card" style="left:620px">
    <div class="stars"><svg width="88" height="15" viewBox="0 0 88 15"><g fill="#f5c61f" stroke="#d9a80f" stroke-width=".5"><use href="#st"/><use href="#st" x="18"/><use href="#st" x="36"/><use href="#st" x="54"/><use href="#st" x="72"/></g></svg></div>
    <h3>Project D</h3>
    <div class="pic" role="img" aria-label="Banknotes wrapped in a chain with a padlock" style="background:linear-gradient(135deg,#6b3b22,#b08a4a 50%,#d4631e)"></div>
    <p>Lorem ipsum dolor sit amet, consectetur adipisicing elit, sed do eiusmod tempor incididunt ut labore et dolore magna aliqua.</p>
    <div class="progress"><b>70 % Success</b></div>
    <div class="invested">90,000 Invested</div>
    <div class="mini" style="left:15px">23,000 Invested</div>
    <div class="mini" style="left:86px">23 Days Left</div>
    <div class="invest-btn">Invest</div>
  </article>

  <div class="abs more">
    <h2>View More Projects</h2>
    <span>More than 1000 projects</span>
    <svg width="32" height="32" viewBox="0 0 32 32"><circle cx="16" cy="16" r="15" fill="#fff"/><path d="M8 16h13M15 10l6 6-6 6" fill="none" stroke="#c9191f" stroke-width="3.5"/></svg>
  </div>
</section>

<section class="abs about">
  <h4 style="left:96px;width:324px">About The Project</h4>
  <div class="photo" role="img" aria-label="Businessman smiling at a desk with a laptop" style="left:97px;width:98px;background:linear-gradient(135deg,#e8e2d8,#8a6b55 50%,#9aa6c4)"></div>
  <p class="body" style="left:204px;width:218px">Lorem ipsum dolor sit amet, consectetur adipisicing elit, sed do eiusmod tempor incididunt ut labore et dolore magna aliqua. Ut enim ad minim veniam, quis nostrud exercitation ullamco laboris nisi ut aliquip ex ea commodo consequat. Duis aute irure dolor in reprehenderit in voluptate velit esse cillum dolore eu fugiat nulla pariatur. Excepteur sint occaecat cupidatat non proident, sunt in culpa qui officia deserunt mollit anim id est laborum</p>
  <span class="read" style="left:375px">Read More</span>

  <h4 style="left:444px;width:336px">Investment Projects</h4>
  <div class="photo" role="img" aria-label="Rolled banknotes beside a safe dial" style="left:446px;width:100px;background:linear-gradient(135deg,#f4f4f2,#a9a9a9 50%,#e9e9e2)"></div>
  <p class="body" style="left:564px;width:216px">Lorem ipsum dolor sit amet, consectetur adipisicing elit, sed do eiusmod tempor incididunt ut labore et dolore magna aliqua. Ut enim ad minim veniam, quis nostrud exercitation ullamco laboris nisi ut aliquip ex ea commodo consequat. Duis aute irure dolor in reprehenderit in voluptate velit esse cillum dolore eu fugiat nulla pariatur. Excepteur sint occaecat cupidatat non proident, sunt in culpa qui officia deserunt mollit anim id est laborum</p>
  <span class="read" style="left:735px">Read More</span>
</section>

<footer class="abs footer">
  <div class="abs social"><i></i><i></i><i></i><i></i></div>
  <div class="abs links"><span>Home</span>|<span>About Us</span>|<span>Services</span>|<span>Blog</span>|<span>FAQs</span>|<span>Contact Us</span></div>
  <div class="abs copy">©&nbsp; 2013 Harvest Cellar ,All&nbsp; rights reserved</div>
</footer>
</body>
</html>
```